'Orla Property Development' Business Card

Business Card Features:

High Quality (potentially textured) thick card - preference is white textured card

Logo (supplied)

We plan to use the vertical logo as the main logo. But i am happy for people to use either if they find it works better for the design of the card.

The building icon and also the insert to the 'E' is in a metallic finish, i think this should be finished in a metallic embossed or raised style.
Updates

Please note i have attached both a horizontal and Vertical Logo for your reference. We plan to use the vertical logo as the main logo. But i am happy for people to use either if they find it works better for the design of the card.

Please note i am considering having the cards made on stainless steel. This introduces the option of having cut outs in the card and etching or printing for the design. If you have a good concept for this please submit.

http://www.quorvantprint.co.uk/black-metal-cards# this is a site that makes the metal cards to offer some direction . . . . Please note i am basic the selection o the best design, if that means normal print cards on paper then this is what i will choose. But there are some great options with the metal. Thanks.

Industry/Entity Type

Building

Requirements
Must have
• Helvetica font to details side of card - logo as supplied to opposite side.

Card Details:

Darren Ashcombe
Managing Director

+61 438 615 207
+61 3 8276 4139

PO Box 73
Bentleigh, VIC 3024

darren@orla.properties

www.orla.properties

```html
<!DOCTYPE html>
<html lang="en">
<head>
<meta charset="utf-8">
<title>Orla Property Development – Business Card</title>
<link rel="stylesheet" href="https://fonts.googleapis.com/css2?family=Arimo:wght@400;700&display=swap">
<style>
  :root {
    --backdrop: #1f1f21;
    --steel-light: #8a8a8c;
    --steel-mid: #6a6a6c;
    --steel-dark: #4a4a4c;
    --ink: #f4f4f4;
    --ink-soft: #d8d8d8;
  }
  html, body {
    margin: 0;
    width: 1200px;
    height: 720px;
    overflow: hidden;
    background: var(--backdrop);
  }
  .canvas {
    width: 1200px;
    height: 720px;
    display: flex;
    align-items: center;
    justify-content: center;
  }
  .card {
    position: relative;
    width: 880px;
    height: 530px;
    border-radius: 6px;
    background:
      repeating-linear-gradient(0deg, rgba(255,255,255,0.035) 0 1px, rgba(0,0,0,0.04) 1px 3px),
      linear-gradient(160deg, var(--steel-dark) 0%, var(--steel-light) 38%, var(--steel-mid) 62%, var(--steel-dark) 100%);
    box-shadow: 0 18px 40px rgba(0,0,0,0.55);
    font-family: Arimo, Helvetica, Arial, sans-serif;
    color: var(--ink);
  }
  .brand {
    position: absolute;
    left: 90px;
    top: 190px;
    display: flex;
    align-items: center;
    gap: 22px;
  }
  .brand-mark {
    width: 26px;
    height: 26px;
    background: var(--ink-soft);
  }
  .brand-name {
    font-size: 30px;
    font-weight: 400;
    color: var(--ink-soft);
    line-height: 1.25;
  }
  .contact {
    position: absolute;
    right: 70px;
    top: 60px;
    text-align: right;
  }
  .contact-name {
    font-size: 30px;
    font-weight: 700;
    margin: 0;
  }
  .contact-role {
    font-size: 18px;
    margin: 4px 0 44px;
    color: var(--ink-soft);
  }
  .details {
    list-style: none;
    margin: 0;
    padding: 0;
    font-size: 18px;
    line-height: 30px;
  }
  .details li {
    display: flex;
    justify-content: flex-end;
    align-items: center;
    gap: 10px;
  }
  .details svg {
    width: 16px;
    height: 16px;
    fill: none;
    stroke: var(--ink);
    stroke-width: 1.6;
  }
  .details .address { color: var(--ink-soft); margin-top: 14px; padding-right: 26px; }
</style>
</head>
<body>
<main class="canvas">
  <section class="card">
    <div class="brand">
      <span class="brand-mark" aria-hidden="true"></span>
      <div class="brand-name">Orla<br>Property Development</div>
    </div>
    <div class="contact">
      <h1 class="contact-name">Darren Ashcombe</h1>
      <p class="contact-role">Managing Director</p>
      <ul class="details">
        <li>0438615207
          <svg viewBox="0 0 16 16" aria-hidden="true"><rect x="4" y="1.5" width="8" height="13" rx="1.5"/><line x1="7" y1="12.2" x2="9" y2="12.2"/></svg>
        </li>
        <li>1800 317 482
          <svg viewBox="0 0 16 16" aria-hidden="true"><path d="M2 6 Q8 1 14 6 L12 8 L10 6.5 L6 6.5 L4 8 Z"/><rect x="4" y="9" width="8" height="5" rx="1"/></svg>
        </li>
        <li>darren@orla.properties
          <svg viewBox="0 0 16 16" aria-hidden="true"><rect x="1.5" y="3.5" width="13" height="9"/><polyline points="1.5,3.5 8,9 14.5,3.5"/></svg>
        </li>
        <li>www.orla.properties
          <svg viewBox="0 0 16 16" aria-hidden="true"><circle cx="8" cy="8" r="6.5"/><ellipse cx="8" cy="8" rx="3" ry="6.5"/><line x1="1.5" y1="8" x2="14.5" y2="8"/></svg>
        </li>
        <li>PO BOX 73 Bentleigh, VIC 3024
          <svg viewBox="0 0 16 16" aria-hidden="true"><polyline points="1.5,8 8,2 14.5,8"/><polyline points="3.5,7 3.5,14 12.5,14 12.5,7"/></svg>
        </li>
      </ul>
    </div>
  </section>
</main>
</body>
</html>
```